Renata Quisby

Luxury And Style -

Black - White & Gold

Target Market(s)

Fashion

Industry/Entity Type

Fashion

Requirements
Must have
• High-End
Nice to have
• We will Print on Silk Paper

```html
<!DOCTYPE html>
<html lang="en">
<head>
<meta charset="utf-8">
<title>Renata Quisby Letterhead</title>
<link rel="stylesheet" href="https://fonts.googleapis.com/css2?family=Marcellus&family=Poppins:wght@300&display=swap">
<style>
  :root {
    --navy: #000229;
    --gold: #c19c6f;
    --gold-text: #b48c62;
    --paper: #ffffff;
  }
  * { margin: 0; padding: 0; box-sizing: border-box; }
  html, body { width: 848px; height: 1200px; overflow: hidden; background: var(--paper); }
  .letterhead { position: relative; width: 848px; height: 1200px; background: var(--paper); overflow: hidden; }
  .letterhead__shapes { position: absolute; inset: 0; }
  .brand { position: absolute; left: 40px; top: 150px; width: 235px; text-align: center; }
  .brand__name {
    font-family: "Marcellus", serif;
    font-weight: 400;
    font-size: 24px;
    letter-spacing: 3.2px;
    color: var(--gold-text);
    text-transform: uppercase;
    white-space: nowrap;
  }
  .brand__tagline {
    margin-top: 4px;
    font-family: "Poppins", sans-serif;
    font-weight: 300;
    font-size: 11px;
    letter-spacing: 0.3px;
    color: var(--gold-text);
    text-transform: uppercase;
  }
  .corner-pattern {
    position: absolute;
    left: 597px; top: 1026px;
    width: 251px; height: 147px;
    background: linear-gradient(135deg, rgba(255,255,255,0) 25%, rgba(0,2,41,0.08) 60%, rgba(0,2,41,0.16) 100%);
  }
</style>
</head>
<body>
<div class="letterhead">
  <svg class="letterhead__shapes" width="848" height="1200" viewBox="0 0 848 1200" aria-hidden="true">
    <path class="header-wave" fill="var(--navy)"
      d="M0 0 H848 V95 C760 125 660 135 600 143 C420 168 250 200 160 245 C100 272 40 320 0 350 Z"/>
    <path class="header-ribbon" fill="var(--gold)"
      d="M99 321 C220 258 360 215 520 190 C660 168 790 158 848 127 V183 C720 190 560 200 420 222 C290 244 170 285 99 321 Z"/>
    <path class="footer-arrow" fill="var(--navy)" d="M0 1138 L50 1167 L0 1195 Z"/>
    <path class="footer-band" fill="var(--gold)" d="M12 1200 L54 1173 H848 V1200 Z"/>
  </svg>

  <div class="brand">
    <div class="brand__name">Renata Quisby</div>
    <div class="brand__tagline">Luxury and Style</div>
  </div>

  <div class="corner-pattern" role="img" aria-label="Decorative cluster of outlined diamond shapes in navy"></div>
</div>
</body>
</html>
```